Modernes Briefpapier für Steuerberater
Zielgruppe
Ich bin Steuerbertaer und brauche ein modernes Briefpapier, was elegant, aber seriös daherkommt.
Aufgabenstellung
Ein Briefpapier mit meinem Logo. Gerne in die Richtung des anderen angehängten Bildes vom Design her.

```html
<!DOCTYPE html>
<html lang="de">
<head>
<meta charset="utf-8">
<title>Kellmann Steuerberatung – Briefpapier</title>
<link rel="stylesheet" href="https://fonts.googleapis.com/css2?family=Roboto:wght@300;400;500&family=Montserrat:wght@600&display=swap">
<style>
:root{
  --backdrop:#e1cdb4;
  --paper:#ffffff;
  --ink:#111111;
  --muted:#707070;
  --brand-blue:#2aa6e0;
  --bar-dark:#3a3a3a;
  --faint:#eeeeee;
}
*{margin:0;padding:0;box-sizing:border-box}
html,body{width:1200px;height:1200px;overflow:hidden;background:var(--backdrop)}
body{position:relative;font-family:"Roboto",Helvetica,Arial,sans-serif;color:var(--ink)}
.sheet{position:absolute;width:505px;height:713px;background:var(--paper);box-shadow:6px 6px 10px rgba(0,0,0,.25);overflow:hidden}
.sheet--first{left:81px;top:251px}
.sheet--follow{left:651px;top:256px}
.sheet > *{z-index:2}
.bar-dark{position:absolute;left:0;top:0;width:9px;height:253px;background:var(--bar-dark)}
.bar-blue{position:absolute;right:0;bottom:0;top:492px;width:9px;background:var(--brand-blue)}
.brand-square{position:absolute;width:41px;height:41px;border:2px solid var(--brand-blue)}
.brand-name{position:absolute;left:53px;top:84px;font-family:"Montserrat",Arial,sans-serif;font-weight:600;font-size:11.5px;letter-spacing:.3px;color:var(--muted);white-space:nowrap}
.contact{position:absolute;left:332px;top:83px;font-size:6.8px;color:var(--muted);font-weight:300}
.contact .person{font-size:9.5px;font-weight:500;color:#444;line-height:1.1}
.contact .role{line-height:1.35;margin-bottom:5px}
.contact .row{line-height:12.8px;white-space:nowrap}
.recipient{position:absolute;left:52px;top:200px;font-size:8.9px;line-height:12.7px;font-weight:300;font-style:normal}
.date{position:absolute;left:332px;top:211px;font-size:9px;font-weight:300}
.customer{position:absolute;left:332px;top:248px}
.customer h2{font-size:10px;font-weight:500}
.customer p{font-size:6.8px;margin-top:4px;font-weight:300}
.salutation{position:absolute;left:52px;top:328px;font-size:9.6px;font-weight:300}
.letter-body{position:absolute;left:52px;top:366px;width:410px;font-size:9.6px;line-height:12.7px;font-weight:300}
.letter-body p+p{margin-top:12.7px}
.watermark{position:absolute;z-index:1;width:186px;height:200px;border:5px solid var(--faint);border-right:none}
.sheet--first .watermark{left:309px;top:517px}
.sheet--follow .watermark{left:308px;top:518px}
.watermark span{position:absolute;left:18px;top:78px;font-family:"Montserrat",Arial,sans-serif;font-weight:600;font-size:26px;color:var(--faint)}
.footer{position:absolute;left:52px;top:658px;width:410px;font-size:5.3px;line-height:9px;color:var(--muted);font-weight:300}
.footer b{font-weight:500}
.fold-mark{position:absolute;left:0;width:18px;height:1px;background:#dcdcdc}
</style>
</head>
<body>

<section class="sheet sheet--first" aria-label="Briefbogen Seite 1">
  <div class="watermark"><span>KELLMANN</span></div>
  <div class="bar-dark"></div>
  <div class="brand-square" style="left:125px;top:33px"></div>
  <div class="brand-name">KELLMANN | STEUERBERATUNG</div>

  <div class="contact">
    <div class="person">Matthias Kellmann</div>
    <div class="role">Dipl.-Betriebswirt (FH)<br>Steuerberater</div>
    <div class="row">Telefon:&nbsp;&nbsp;&nbsp;&nbsp; +49 (0) 00 07 / 4 2810</div>
    <div class="row">Telefax:&nbsp;&nbsp;&nbsp;&nbsp;&nbsp; +49 (0) 00 07 / 4 2811</div>
    <div class="row">E-Mail:&nbsp; post@kellmann-steuer.de</div>
    <div class="row">Internet: www.kellmann-steuer.de</div>
    <div class="row">USt-ID: DE000123456</div>
  </div>

  <address class="recipient">
    Lukas Verhoeven<br>Firma Verhoeven<br>Lindenweg 12<br>96100 Musterau
  </address>

  <div class="date">Talbrück, 29. April 2019</div>

  <div class="customer">
    <h2>Ihre Kundendaten</h2>
    <p>Kundennummer: 40200815</p>
  </div>

  <div class="salutation">Lorem ipsum dolor sit amet,</div>

  <div class="letter-body">
    <p>Lorem ipsum dolor sit amet, consectetur adipiscing elit. Donec orci purus, luctus vitae dignis&shy;sim eu, iaculis sed purus. Vivamus faucibus, ipsum nec aliquet viverra, leo mauris condimen&shy;tum ligula, sit amet sagittis enim ligula quis arcu. Nam egestas tortor id nisi porttitor mattis. In tortor ante, ultricies in suscipit a, tempus non massa. Vivamus et auctor mi. Fusce vel massa nulla. Phasellus nec eros mauris, et scelerisque orci. Donec malesuada orci vitae nulla accumsan porta a id massa. Quisque accumsan iaculis magna sit amet fringilla. Maecenas consequat, magna eget tincidunt semper, odio nibh rutrum mi, id feugiat ante nisi eu risus. Vestibulum nunc orci, rhoncus a placerat in, ultricies in mi. Cras mattis varius eros, vel fringilla nisi suscipit eget.</p>
    <p>Quisque scelerisque sagittis nulla at porttitor. Mauris a justo et tellus interdum tristique. Sed id augue vitae urna euismod commodo aliquet a quam. Pellentesque arcu velit, cursus et male&shy;suada ut, consequat et diam. Nullam erat sem, rhoncus id ullamcorper vitae, rhoncus et arcu. In ultricies ultricies nulla, ut rutrum nisi iaculis at. Donec eu magna a metus ornare faucibus.</p>
  </div>

  <div class="footer">
    <b>M. Kellmann</b> | Steuerberatung<br>
    Am Markt 4 | 59000 Feldheim (Germany) | Geschäftsführer: Anna Feldmann Registergericht: Amtsgericht Feldheim Handelsregister: HRB 10000 Umsatzsteuer-ID: DE 100200300 | <b>Bankverbindung</b> Kontoinhaber: KELLMANN STEUERBERATUNG GMBH | IBAN: DE00 1234 5678 0000 0000 00<br>
    SWIFT-BIC: FELDDE11 | Bank: Sparkasse Feldheim
  </div>

  <div class="bar-blue"></div>
</section>

<section class="sheet sheet--follow" aria-label="Briefbogen Folgeseite">
  <div class="watermark"><span>KELLMANN</span></div>
  <div class="bar-dark"></div>
  <div class="fold-mark" style="top:253px"></div>
  <div class="fold-mark" style="top:492px"></div>
  <div class="brand-square" style="left:417px;top:20px"></div>
  <div class="bar-blue"></div>
</section>

</body>
</html>
```